Give Tall Oak Ridge an Online Presence!

Tall Oak Ridge Property Maintenance is an Australian Owned property maintenance company who needs a stand out online presence.

TOR maintains many buildings and sites and wants to appeal to a corporate professional market with their brand new website. TOR is essentially a handyman service offering all maintenance services to home owners, office managers, real estate agents and strata managers.

The Website:
We need a corporate website that appeals to our broader customer base (property owners, property managers, office managers) the copy is being written by a professional so use filler text for now.

Things that we want:
Home page that sets us apart and appeals to the corporate and residential market. The home page needs to not focus on either the residential or commercial market. The home page should focus on our logo and branding. We have a logo already and it is attached to the brief, please use it and try to consider the colour pallette that goes with it. Whilst we want the site to appear strong and manly it is important to remember that 95% of our customers are female so we need the site to be appealing to women. Women need to believe that we are strong, dependable and trustworthy.
We'd like a quote page and potentially also the ability to get a quote from the home page (please don't put it in if it ruins the overall feel of the home page)
An "about us" page
A contact us page
A blog that's built in (we don't want to link to an external blog)
(overall we'd expect to have 6 or 7 pages total)

The site will also need coding - we expect this to be done in a separate project but need you to consider a few things about the coding side of things.

It needs to be iPhone and iPad compatible.

We'd like you to suggest the best CMS that you would use or if you would suggest not using a CMS please let us know with your submissions.

Target Market(s)

Property owners, office managers and property managers who need maintenance on buildings (So all of them)

Industry/Entity Type

Property Maintenance

Requirements
Must have
• Our Logo
Home page
About Us
Residential
Commercial
Real Estate/Strata
Contact Us/Quote
Blog
Nice to have
• Quote form included in home page
Movement on the home page at least
Should not have
• other logos, too much colour
NO FLASH

```html
<!DOCTYPE html>
<html lang="en">
<head>
<meta charset="utf-8">
<title>Tall Oak Ridge Property Maintenance</title>
<link href="https://fonts.googleapis.com/css2?family=PT+Sans+Narrow:wght@400;700&family=Open+Sans:wght@400;600&family=Lato:wght@400;700&display=swap" rel="stylesheet">
<style>
:root{
  --orange:#f07d1a;
  --orange-dark:#e2610f;
  --orange-light:#f79a32;
  --ink:#222;
  --text:#4a4a4a;
  --muted:#666;
  --line:#e3e3e3;
  --page:#ececec;
  --white:#fff;
}
*{box-sizing:border-box;margin:0;padding:0}
html,body{width:871px;height:1200px;overflow:hidden}
body{position:relative;background:var(--page);font-family:'Lato',sans-serif;color:var(--text)}
.topline{position:absolute;left:0;top:0;width:871px;height:4px;background:#2b2b2b}
.header-bg{position:absolute;left:0;top:4px;width:871px;height:384px;background:linear-gradient(180deg,#fafafa,#f1f1f1 70%,#e9e9e9)}
.lower-bg{position:absolute;left:0;top:388px;width:871px;height:732px;background:#f4f4f4}
.brand{position:absolute;left:48px;top:40px;display:flex;align-items:center;gap:8px}
.brand-mark{width:26px;height:26px;background:var(--orange);border-radius:50%}
.brand-name{font-family:'PT Sans Narrow',sans-serif;font-weight:700;font-size:19px;color:var(--orange-dark);line-height:1.05;width:110px}
.callus{position:absolute;right:102px;top:70px;font-family:'Open Sans',sans-serif;font-size:15px;color:var(--ink);white-space:nowrap}
.social{position:absolute;display:flex;gap:3px}
.social span{width:21px;height:21px;border-radius:50%;background:#1b1b1b;display:block}
.social.head{left:782px;top:70px}
.social.foot{left:774px;top:1130px}
.social.foot span{width:24px;height:24px;background:#555}
.search{position:absolute;left:618px;top:106px;width:210px;height:24px;background:var(--white);border:1px solid #ddd;font-family:'Open Sans',sans-serif;font-size:10px;color:#888;padding:5px 8px}
.search svg{position:absolute;right:6px;top:5px}
.nav{position:absolute;left:38px;top:143px;width:796px;height:42px;background:linear-gradient(180deg,var(--orange-light),var(--orange-dark));display:flex;border-radius:3px 3px 0 0}
.nav a{font-family:'Open Sans',sans-serif;font-size:11px;color:var(--white);text-decoration:none;display:flex;align-items:center;justify-content:center;border-right:1px solid rgba(0,0,0,.12);height:100%}
.hero{position:absolute;left:38px;top:185px;width:524px;height:289px;background:var(--white)}
.hero-photo{position:absolute;left:3px;top:4px;width:392px;height:285px;background:linear-gradient(90deg,#e8c9a8 0,#d9a36e 30%,#3a78b8 52%,rgba(255,255,255,0) 66%),linear-gradient(180deg,#f3eee6,#e7d7c2)}
.hero-copy{position:absolute;left:274px;top:55px;width:240px;z-index:1}
.hero-copy .kicker{font-family:'PT Sans Narrow',sans-serif;font-weight:700;font-size:20px;color:var(--ink);white-space:nowrap}
.hero-copy h1{font-family:'PT Sans Narrow',sans-serif;font-weight:700;font-size:24px;color:var(--orange-dark);line-height:1.1;white-space:nowrap}
.hero-copy p{font-family:'PT Sans Narrow',sans-serif;font-size:11.5px;color:var(--ink);line-height:1.4;margin-top:3px;width:215px}
.slide{position:absolute;left:562px;width:271px;background:var(--white)}
.slide-photo{height:107px}
.slide-cap{height:36px;display:flex;align-items:center;justify-content:space-between;padding:0 16px 0 15px;font-family:'PT Sans Narrow',sans-serif;font-size:16px;color:#333}
.slide.one{top:186px}
.slide.one .slide-photo{background:linear-gradient(160deg,#6a4a2c,#b08050 55%,#f2c23a)}
.slide.two{top:330px}
.slide.two .slide-photo{background:linear-gradient(160deg,#c8cdd2,#8a8f8a 50%,#e0532a 80%)}
.hero-shadow{position:absolute;left:44px;top:476px;width:790px;height:10px;background:radial-gradient(ellipse at center top,rgba(0,0,0,.22),transparent 70%)}
.feature{position:absolute;top:498px;height:128px;background:var(--white);border:1px solid var(--line);overflow:hidden}
.feature h2{position:absolute;left:18px;top:13px;font-family:'PT Sans Narrow',sans-serif;font-weight:700;font-size:17px;color:var(--ink);z-index:1;white-space:nowrap}
.feature p{position:absolute;left:18px;top:36px;width:118px;font-family:'PT Sans Narrow',sans-serif;font-size:10px;line-height:15.5px;color:#444;z-index:1}
.btn{position:absolute;background:var(--orange);color:var(--white);font-family:'Open Sans',sans-serif;font-size:9.5px;padding:3px 8px}
.feature .btn{left:16px;top:91px;z-index:1}
.feature-photo{position:absolute;right:0;top:0;width:100px;height:126px}
.f1{left:38px;width:248px}.f1 .feature-photo{background:linear-gradient(135deg,#fff,#f3e6c8 45%,#d24a2a 70%,#fff)}
.f2{left:308px;width:257px}.f2 .feature-photo{background:linear-gradient(135deg,#d9c4a8,#b07a40 50%,#f0f0f0)}
.f3{left:578px;width:250px}.f3 .feature-photo{background:linear-gradient(135deg,#f1ede6,#cf3a2e 50%,#d4b48a)}
.blog{position:absolute;left:38px;top:652px;width:526px;height:454px;background:var(--white);border:1px solid var(--line)}
.blog h2{position:absolute;left:17px;top:14px;font-family:'PT Sans Narrow',sans-serif;font-weight:700;font-size:19px;color:var(--ink)}
.blog .intro{position:absolute;left:17px;top:41px;font-family:'PT Sans Narrow',sans-serif;font-size:10px;color:#444}
.post{position:absolute;left:16px;width:495px}
.post-photo{position:absolute;left:0;top:-5px;width:128px;height:82px}
.post-body{position:absolute;left:142px;top:0;width:352px}
.post h3{font-family:'PT Sans Narrow',sans-serif;font-weight:700;font-size:12.5px;color:#333}
.post p{font-family:'Lato',sans-serif;font-size:9.5px;line-height:15.6px;color:#555;margin-top:3px}
.post .meta{font-family:'PT Sans Narrow',sans-serif;font-size:10.5px;color:#444;margin-top:3px}
.p1{top:80px}.p1 .post-photo{background:linear-gradient(135deg,#6b5440,#c9643c 50%,#a47a52)}
.p2{top:220px}.p2 .post-photo{background:linear-gradient(135deg,#2b7fd0,#5fa6e6 50%,#c9e35a)}
.p3{top:335px}.p3 .post-photo{background:linear-gradient(135deg,#e9e2d6,#9a6a3e 50%,#b25a30)}
.rule{position:absolute;left:18px;width:490px;border-top:1px dotted #bbb}
.contact{position:absolute;left:572px;top:652px;width:263px;height:454px;background:linear-gradient(180deg,var(--orange) 0,var(--orange-dark) 100%);border-radius:3px}
.contact h2{position:absolute;left:20px;top:12px;font-family:'PT Sans Narrow',sans-serif;font-weight:700;font-size:20px;color:var(--white)}
.contact .sub{position:absolute;left:20px;top:38px;font-family:'PT Sans Narrow',sans-serif;font-weight:700;font-size:10px;color:var(--white)}
.contact .divider{position:absolute;left:0;top:59px;width:263px;border-top:1px solid rgba(255,255,255,.25)}
.field-label{position:absolute;left:19px;font-family:'Open Sans',sans-serif;font-weight:600;font-size:9.5px;color:var(--white)}
.field{position:absolute;left:19px;width:220px;height:24px;background:var(--white);border-radius:2px}
.contact .btn{left:20px;top:376px;background:var(--orange-light);font-weight:600;font-size:10px;padding:4px 12px}
.footer{position:absolute;left:0;top:1120px;width:871px;height:80px;background:#ececec}
.footer-links{position:absolute;left:37px;top:18px;font-family:'Open Sans',sans-serif;font-size:9.5px;color:#222}
.footer-links span{color:#999;margin:0 6px}
.copy{position:absolute;left:37px;top:43px;font-family:'Open Sans',sans-serif;font-size:8.5px;color:#333}
</style>
</head>
<body>
<div class="topline"></div>
<div class="header-bg"></div>
<div class="lower-bg"></div>

<header>
  <div class="brand"><span class="brand-mark"></span><span class="brand-name">Tall Oak Ridge</span></div>
  <div class="callus">CALL US +685 555 0142</div>
  <div class="social head"><span aria-label="Social link"></span><span aria-label="Social link"></span></div>
  <div class="search">enter keyword
    <svg width="13" height="13" viewBox="0 0 13 13"><circle cx="5.5" cy="5.5" r="4" fill="none" stroke="#777" stroke-width="1.6"/><line x1="8.5" y1="8.5" x2="12" y2="12" stroke="#777" stroke-width="1.8"/></svg>
  </div>
  <nav class="nav">
    <a href="#" style="width:87px">HOME</a>
    <a href="#" style="width:87px">ABOUT US</a>
    <a href="#" style="width:100px">RESIDENTIAL</a>
    <a href="#" style="width:104px">COMMERCIAL</a>
    <a href="#" style="width:146px">REAL ESTATE/STRATA</a>
    <a href="#" style="width:100px">CONTACT US</a>
    <a href="#" style="width:70px;border-right:0">BLOG</a>
  </nav>
</header>

<section class="hero">
  <div class="hero-photo" role="img" aria-label="Smiling tradeswoman holding paint rollers and brushes, giving a thumbs up"></div>
  <div class="hero-copy">
    <div class="kicker">24/7 Services Available</div>
    <h1>HOUSING MAINTENANCE</h1>
    <p>Mauris vel lacus vitae felis vestibulum volutpat. Etiam est nunc, venenatis in, tristique eu, imperdiet ac, nisl. Cum sociis natoque</p>
  </div>
</section>

<div class="slide one">
  <div class="slide-photo" role="img" aria-label="Worker in a yellow hard hat"></div>
  <div class="slide-cap">Ut velit enim, vestibulum non
    <svg width="26" height="26" viewBox="0 0 26 26"><circle cx="13" cy="13" r="11.5" fill="none" stroke="#222" stroke-width="2"/><path d="M10.5 8.5 L17.5 13 L10.5 17.5Z" fill="#222"/></svg>
  </div>
</div>
<div class="slide two">
  <div class="slide-photo" role="img" aria-label="Engineers in hard hats reviewing plans on site"></div>
  <div class="slide-cap">Purus nisi eleifend libero
    <svg width="26" height="26" viewBox="0 0 26 26"><circle cx="13" cy="13" r="11.5" fill="none" stroke="#222" stroke-width="2"/><path d="M10.5 8.5 L17.5 13 L10.5 17.5Z" fill="#222"/></svg>
  </div>
</div>
<div class="hero-shadow"></div>

<section class="feature f1">
  <h2>Featured Service</h2>
  <p>Lorem ipsum dolor sit amet, consectetuer adipiscing elit. Nam cursus.</p>
  <a class="btn">Learn More</a>
  <div class="feature-photo" role="img" aria-label="Small model house with a wrench"></div>
</section>
<section class="feature f2">
  <h2>Featured Service</h2>
  <p>Lorem ipsum dolor sit amet, consectetuer adipiscing elit. Nam cursus.</p>
  <a class="btn">Learn More</a>
  <div class="feature-photo" role="img" aria-label="Tool belt with hammer and screwdrivers"></div>
</section>
<section class="feature f3">
  <h2>Featured Service</h2>
  <p>Lorem ipsum dolor sit amet, consectetuer adipiscing elit. Nam cursus.</p>
  <a class="btn">Learn More</a>
  <div class="feature-photo" role="img" aria-label="Woman sawing timber on a workbench"></div>
</section>

<section class="blog">
  <h2>Recent Blog Post</h2>
  <div class="intro">Lorem ipsum dolor sit amet, consectetuer adipiscing elit. Nam cursus.</div>
  <article class="post p1">
    <div class="post-photo" role="img" aria-label="Woman using a power drill on a wall"></div>
    <div class="post-body">
      <h3>Headline goes here</h3>
      <p>Duis non nunc. Nulla rhoncus dictum metus. Curabitur tristique mi condimentum orci. Phasellus pellentesque aliquam enim. Proin dui lectus, cursus eu, mattis laoreet, viverra sit amet, quam. Curabitur vel dolor ultrices ipsum dictum tristique. Praesent vitae lacus. Ut velit enim, vestibulum non, fermentum nec, hendrerit quis, leo. Pellentesque rutrum malesuada neque.</p>
      <div class="meta">Posted 2 hours ago &nbsp;|&nbsp; Learn More</div>
    </div>
  </article>
  <div class="rule" style="top:198px"></div>
  <article class="post p2">
    <div class="post-photo" role="img" aria-label="Woman painting a wall blue with a roller"></div>
    <div class="post-body">
      <h3>Headline goes here</h3>
      <p>Duis non nunc. Nulla rhoncus dictum metus. Curabitur tristique mi condimentum orci. Phasellus pellentesque aliquam enim. Proin dui lectus, cursus eu, mattis laoreet, viverra sit amet, quam. Curabitur vel dolor ultrices ipsum dictum tristique.</p>
      <div class="meta">Posted 2 hours ago &nbsp;|&nbsp; Learn More</div>
    </div>
  </article>
  <div class="rule" style="top:313px"></div>
  <article class="post p3">
    <div class="post-photo" role="img" aria-label="Couple assembling flat pack furniture"></div>
    <div class="post-body">
      <h3>Headline goes here</h3>
      <p>Duis non nunc. Nulla rhoncus dictum metus. Curabitur tristique mi condimentum orci. Phasellus pellentesque aliquam enim. Proin dui lectus, cursus eu, mattis laoreet, viverra sit amet, quam. Curabitur vel dolor ultrices ipsum dictum tristique.</p>
      <div class="meta">Posted 2 hours ago &nbsp;|&nbsp; Learn More</div>
    </div>
  </article>
</section>

<aside class="contact">
  <h2>Fill Our Contact Form</h2>
  <div class="sub">Lorem ipsum dolor sit amet, consectetuer adipiscing</div>
  <div class="divider"></div>
  <label class="field-label" style="top:73px">Name</label><div class="field" style="top:89px"></div>
  <label class="field-label" style="top:121px">Phone no.</label><div class="field" style="top:137px"></div>
  <label class="field-label" style="top:172px">Email address</label><div class="field" style="top:186px"></div>
  <label class="field-label" style="top:221px">Address</label><div class="field" style="top:235px"></div>
  <label class="field-label" style="top:269px">Message</label><div class="field" style="top:283px;height:81px"></div>
  <a class="btn">SUBMIT</a>
</aside>

<footer class="footer">
  <div class="footer-links">Home<span>|</span>About Us<span>|</span>Residential<span>|</span>Commercial<span>|</span>Real Estate/Strata<span>|</span>Contact Us<span>|</span>Blog</div>
  <div class="copy">Copyright © 2012 Company Name. Term of Use. &nbsp;All right reserved</div>
</footer>
<div class="social foot"><span aria-label="Social link"></span><span aria-label="Social link"></span></div>
</body>
</html>
```